FULLY CUSTOM MAIN BANNER IMAGE FOR MY WEBSITE-REDESIGN CURRENT

SIZE MUST BE: 1800x829

LOOKING FOR A FULLY CUSTOM MAIN BANNER IMAGE TO BE DESIGNED FOR MY NEW WEBSITE HOMEPAGE http://pixelquarry-demo.net/qa/dorin/vtl_draft/index.html THE CONTENT THAT YOU SEE ON THE UPLOADED FILE OR HERE http://pixelquarry-demo.net/qa/dorin/vtl_draft/index.html YOU CAN SEE MY EXISTING BANNER IMAGE...IS THE SAME CONTENT I WANT ON THE CUSTOM BANNER IMAGE BUT I WANT THE BANNER IMAGE TO USE IMAGES TO PORTRAY WHAT THE CONTENT SAYS. POSSIBLE INTEGRATE AN INFOGRAPHIC DESIGN IN THE BANNER IMAGE. IM OPEN TO ALL IDEAS.

WHEN SOMEONE GOES TO MY WEBSITE, IMMEDIATELY I WANT THEM TO UNDERSTAND WHAT IT IS I DO.

MY BUSINESS PROVIDES OTHER BUSINESSES WITH THE ABILITY TO CREATE PROMOTIONAL GIVEAWAYS AND MARKETING PROMOTIONS USING GIFT VOUCHERS THAT ARE REDEEMABLE FOR FREE VACATIONS, CRUISES, ALL INCLUSIVE RESORT STAYS, TABLETS, SMARTWATCHES, DINING AND RESTAURANT INCENTIVES AND REWARDS AND MORE.

CURRENTLY THE CONTENT ON THE BANNER IMAGE IS THIS:
BOOST SALES & LEADS OVERNIGHT
BY ENTICING YOUR CUSTOMERS WITH FREE VACATION CERTIFICATES & OTHER HIGH PERCEIVED VALUE INCENTIVES

I HAVE ATTACHED A DOCUMENT WITH IMAGE ASSETTS YOU MAY REVIEW AND USE OR GET IDEAS FROM.

THE BOTTOM LINE IS MY SERVICE HELPS BUSINESSES INCREASE LEADS, CONVERSIONS, CTA, SALES, ETC WITHOUT HAVING TO INCREASE THEIR EXISTING AD SPEND. SIMPLY BY ADDING A FREE OFFER TO ALL THEIR EXISTING ADS WILL DRAMATICALLY INCREASE RESPONSE RATES. SO I WANT THIS BANNER TO REFLECT THIS SOMEHOW....MORE CUSTOMERS USING GIVEAWAYS!

Target Market(s)

B2B, SMALL BUSINESS OWNERS, ENTREPRENEURS, SOLOPRENEURS, MARKETING AGENCIES,

Industry/Entity Type

Digital Marketing

Requirements
Must have
• MUST PORTRAY THE RED CONTENT/TEXT USING IMAGES OF MY ASSETTS AND THE PORTRAY MORE CUSTOMERS---MUST BE FULLY CUSTOM

SIZE MUST BE: 1800x829
Nice to have
• USE CONTENT IN CURRENT BANNER IMAGE ALSO MAKE SURE TO USE THE FREE SAMPLE PKG BUTTON TOO.....MUST BE FULLY CUSTOM

SIZE MUST BE: 1800x829
Should not have
• MUST BE FULLY CUSTOM

SIZE MUST BE: 1800x829

```html
<!DOCTYPE html>
<html lang="en">
<head>
<meta charset="utf-8">
<title>Boost Sales &amp; Leads Overnight – Homepage Banners</title>
<link href="https://fonts.googleapis.com/css2?family=Poppins:wght@400;600;700;800&family=Oswald:wght@500;600&display=swap" rel="stylesheet">
<style>
  :root{
    --page:#ffffff;
    --navy:#33374a;
    --navy-deep:#262a3a;
    --tile-dark:#1d2029;
    --orange:#ee8a0f;
    --orange-light:#f7a21c;
    --orange-dark:#d0740a;
    --headline-orange:#f7941d;
    --teal:#12a3b0;
    --blue:#1b5fa6;
    --submit:#1f74c9;
    --white:#ffffff;
    --brand-brown:#6b3a12;
    --red:#d61f26;
    --pink:#d0245a;
    --green:#4cc33b;
    --field:#e9ebef;
    --ink:#2a2d38;
  }
  *{box-sizing:border-box;margin:0;padding:0}
  html,body{width:1200px;height:1136px;overflow:hidden;background:var(--page)}
  body{position:relative;font-family:'Poppins',sans-serif;color:var(--white)}

  .banner{position:absolute;left:25px;width:1149px;height:530px;overflow:hidden}
  .banner--collage{top:25px;background:var(--navy-deep)}
  .banner--showcase{top:581px;background:var(--navy)}

  /* tilted offer collage */
  .collage-grid{position:absolute;left:-300px;top:-330px;width:1240px;height:1160px;
    display:flex;gap:12px;transform:rotate(-30deg);transform-origin:50% 50%}
  .collage-col{width:190px;flex:none;display:flex;flex-direction:column;gap:12px}
  .tile{position:relative;width:100%;flex:none;overflow:hidden}
  .tile--band{height:58px;display:flex;align-items:center;justify-content:center;text-align:center;
    font-family:'Oswald',sans-serif;font-weight:600;font-size:21px;line-height:23px;letter-spacing:.5px}
  .tile--pink{background:var(--pink)}
  .tile--green{background:var(--green)}
  .tile--red{background:var(--red)}
  .tile--dark{background:var(--tile-dark)}
  .tile--form{height:236px;background:var(--tile-dark);padding:14px 12px}
  .form__title{font-family:'Oswald',sans-serif;font-weight:600;font-size:18px;line-height:19px;color:var(--green)}
  .form__lead{font-family:'Oswald',sans-serif;font-size:7.5px;line-height:11px;color:#dfe2ea;margin-top:5px}
  .form__lead b{color:var(--orange-light);font-weight:500}
  .form__field{height:18px;background:var(--field);margin-top:7px;width:120px;font-size:6px;color:#888;padding:5px 4px}
  .form__submit{height:20px;width:120px;background:var(--submit);margin-top:8px;font-family:'Oswald',sans-serif;font-size:8px;text-align:center;line-height:20px}
  .form__fine{font-family:'Oswald',sans-serif;font-size:5.5px;line-height:8px;color:#cfd2da;margin-top:8px;width:120px}

  .offer-wedge{position:absolute;inset:0}

  .collage-copy{position:absolute;right:17px;top:0;text-align:right;width:560px}
  .headline{font-weight:800;font-size:51px;line-height:52px;letter-spacing:-0.5px}
  .collage-copy .headline{position:absolute;right:0;top:24px;white-space:nowrap}
  .subhead{font-weight:700;font-size:29px;line-height:46px;white-space:nowrap}
  .collage-copy .subhead{position:absolute;right:0;top:146px}
  .limited{font-weight:400;font-size:22px;white-space:nowrap}
  .collage-copy .limited{position:absolute;right:-4px;top:297px}

  .cta{position:absolute;border-radius:40px;text-align:center;color:var(--white)}
  .cta__label{display:block;font-weight:600;font-size:40px;line-height:40px;letter-spacing:0.3px}
  .cta__note{display:block;font-weight:600;font-size:12px;line-height:14px;margin-top:2px}
  .cta--teal{left:689px;top:346px;width:443px;height:75px;padding-top:10px;
    background:linear-gradient(90deg,var(--blue),var(--teal));border:2px solid #0d7f96}
  .cta--orange{left:38px;top:381px;width:402px;height:76px;padding-top:11px;
    background:linear-gradient(180deg,var(--orange-light),var(--orange-dark))}

  .brand-name{position:absolute;left:772px;top:440px;width:162px;text-align:center;
    font-weight:800;font-size:50px;line-height:60px;color:var(--brand-brown)}

  .showcase-backdrop{position:absolute;inset:0;
    background:radial-gradient(circle at 55% 30%,#3c4055 0%,#33374a 55%,#2c3042 100%)}
  .showcase-copy{position:absolute;left:38px;top:0}
  .showcase-copy .headline{position:absolute;left:0;top:58px;color:var(--headline-orange);white-space:nowrap}
  .showcase-copy .subhead{position:absolute;left:0;top:182px}
  .showcase-copy .limited{position:absolute;left:0;top:333px}

  /* sample flyers */
  .flyer{position:absolute;overflow:hidden;box-shadow:0 8px 20px rgba(0,0,0,.4)}
  .flyer--signup{left:574px;top:120px;width:224px;height:290px;background:var(--tile-dark);transform:skewY(-4deg)}
  .signup__title{position:absolute;left:8px;top:28px;font-family:'Oswald',sans-serif;font-weight:600;
    font-size:15px;line-height:17px;color:var(--green)}
  .signup__lead{position:absolute;left:8px;top:68px;font-family:'Oswald',sans-serif;font-size:7px;line-height:11px;color:#dfe2ea}
  .signup__lead b{color:var(--orange-light)}
  .signup__photo{position:absolute;right:0;top:0;width:110px;height:200px;background:linear-gradient(160deg,#6b4a3a,#2f2a2c)}
  .signup__field{position:absolute;left:8px;width:84px;height:18px;background:var(--field);
    font-size:6px;color:#888;padding:5px 4px}
  .signup__submit{position:absolute;left:8px;top:190px;width:84px;height:22px;background:var(--submit);
    font-family:'Oswald',sans-serif;font-size:8px;text-align:center;line-height:22px}
  .signup__fine{position:absolute;left:8px;top:222px;width:90px;font-family:'Oswald',sans-serif;font-size:5.5px;line-height:8px;color:#cfd2da}

  .flyer--restaurant{left:689px;top:233px;width:156px;height:248px;background:#fff;transform:skewY(-4deg)}
  .restaurant__bar{position:absolute;left:0;top:0;width:100%;height:26px;background:var(--green);
    font-family:'Oswald',sans-serif;font-size:11px;text-align:center;line-height:26px}
  .restaurant__photo{position:absolute;left:0;top:26px;width:100%;height:160px;background:linear-gradient(180deg,#8a6a58,#4a3a34)}
  .restaurant__foot{position:absolute;left:0;bottom:0;width:100%;height:62px;background:var(--red);
    font-family:'Oswald',sans-serif;font-weight:600;font-size:15px;line-height:18px;text-align:center;padding-top:12px}

  .flyer--earbuds{left:858px;top:38px;width:239px;height:443px;background:#fff;color:var(--ink);transform:skewY(-4deg)}
  .earbuds__hero{position:absolute;left:0;top:0;width:100%;height:190px;background:linear-gradient(135deg,#e4e5e8,#a88c7a)}
  .earbuds__title{position:absolute;left:10px;top:14px;font-family:'Oswald',sans-serif;font-weight:600;font-size:30px;line-height:32px;color:#555}
  .earbuds__tag{position:absolute;left:82px;top:40px;background:var(--red);color:#fff;font-family:'Oswald',sans-serif;font-size:12px;padding:1px 4px}
  .earbuds__band{position:absolute;left:0;top:190px;width:100%;height:20px;background:var(--red);color:#fff;font-size:6px;padding:6px 10px;font-weight:600}
  .earbuds__text{position:absolute;left:10px;top:216px;width:170px;font-size:5.5px;line-height:8px}
  .earbuds__label{position:absolute;left:8px;background:var(--navy);color:#fff;font-size:6px;font-weight:700;padding:2px 6px;border-radius:6px}
  .earbuds__label--red{background:var(--red)}
  .earbuds__cert{position:absolute;left:10px;bottom:12px;width:219px;height:44px;border:1px dashed #999;font-size:5.5px;padding:5px;line-height:8px}
  .earbuds__cert strong{color:var(--red);font-size:9px}
  .earbuds__url{position:absolute;right:6px;top:12px;color:var(--red);font-weight:800;font-size:9px}
  .earbuds__dots{position:absolute;right:6px;top:200px;width:40px}
  .earbuds__dots span{display:block;width:40px;height:40px;border-radius:50%;border:3px solid var(--red);background:#7a5a4c;margin-bottom:10px}
</style>
</head>
<body>

<section class="banner banner--collage">
  <div class="collage-grid">
    <div class="collage-col" style="margin-top:40px">
      <div class="tile" style="height:260px;background:linear-gradient(180deg,#a9cde8,#5e8fb8)" role="img" aria-label="Photo of an airliner in a blue sky"></div>
      <div class="tile tile--red" style="height:40px"></div>
      <div class="tile" style="height:260px;background:linear-gradient(180deg,#8fb7d6,#4f7f9e)" role="img" aria-label="Photo of a seaside city skyline"></div>
      <div class="tile tile--band tile--dark">VIVA ORLANDO</div>
      <div class="tile" style="height:260px;background:linear-gradient(180deg,#6c95b8,#3f6888)" role="img" aria-label="Photo of a coastal resort"></div>
    </div>
    <div class="collage-col" style="margin-top:-40px">
      <div class="tile" style="height:220px;background:linear-gradient(180deg,#8a7664,#d7cdc2)" role="img" aria-label="Photo of a hotel room with a made bed"></div>
      <div class="tile tile--band tile--pink">2 NIGHT HOTEL STAY</div>
      <div class="tile" style="height:250px;background:linear-gradient(180deg,#6fa7d6,#3b7d73)" role="img" aria-label="Photo of a tropical beach resort with palm trees"></div>
      <div class="tile tile--band tile--dark">LUXURIOUS MEXICO<br>BEACH RESORT</div>
      <div class="tile tile--form">
        <div class="form__title">GET A<br>FREE SAMPLE</div>
        <div class="form__lead">ENTER YOUR DETAILS BELOW TO GET<br>YOUR FREE SAMPLE<br><b>TWO NIGHT GETAWAY TO<br>VIVA LAS VEGAS!</b></div>
        <div class="form__field">Name</div><div class="form__field">Email</div><div class="form__field">Phone</div>
        <div class="form__submit">SUBMIT</div>
        <div class="form__fine">Receive a sample by email, text message and an instant pdf download.</div>
      </div>
      <div class="tile tile--band tile--red">REDEEM OFFER NOW</div>
    </div>
    <div class="collage-col" style="margin-top:20px">
      <div class="tile tile--form" style="height:150px"></div>
      <div class="tile tile--band tile--green">REDEEM OFFER NOW</div>
      <div class="tile" style="height:250px;background:linear-gradient(180deg,#5aa0c4,#3f8a78)" role="img" aria-label="Photo of a resort pool with thatched umbrellas"></div>
      <div class="tile tile--form">
        <div class="form__title">GET A<br>FREE SAMPLE</div>
        <div class="form__lead">ENTER YOUR DETAILS BELOW TO GET<br>YOUR FREE SAMPLE<br><b>1 NIGHT HOTEL STAY</b></div>
        <div class="form__field">Name</div><div class="form__field">Email</div><div class="form__field">Phone</div>
        <div class="form__submit">SUBMIT</div>
        <div class="form__fine">Receive a sample by email, text message and an instant pdf download.</div>
      </div>
      <div class="tile" style="height:220px;background:linear-gradient(180deg,#c9a46a,#7c5a8e)" role="img" aria-label="Las Vegas sign and skyline"></div>
      <div class="tile tile--band tile--red">REDEEM OFFER NOW</div>
    </div>
    <div class="collage-col" style="margin-top:-60px">
      <div class="tile" style="height:200px;background:linear-gradient(180deg,#e9e9ec,#b9bcc4)" role="img" aria-label="Printed offer sheet with features list"></div>
      <div class="tile" style="height:200px;background:linear-gradient(180deg,#7aa7a0,#4a5a66)" role="img" aria-label="Photo of a hotel lobby"></div>
      <div class="tile" style="height:270px;background:linear-gradient(180deg,#6a4b3c,#c7a488)" role="img" aria-label="Photo of a couple dining with wine"></div>
      <div class="tile tile--band tile--red">$100 RESTAURANT<br>CERTIFICATE</div>
      <div class="tile" style="height:220px;background:linear-gradient(180deg,#7c8a5a,#4a3a34)" role="img" aria-label="Photo of wine and grapes"></div>
    </div>
    <div class="collage-col" style="margin-top:10px">
      <div class="tile" style="height:160px;background:linear-gradient(180deg,#d9b7a3,#b78a74)" role="img" aria-label="Smiling models with white teeth"></div>
      <div class="tile tile--form">
        <div class="form__title">GET A<br>FREE SAMPLE</div>
        <div class="form__lead">ENTER YOUR DETAILS BELOW TO GET<br>YOUR FREE SAMPLE<br><b>PROFESSIONAL GRADE HOME<br>TEETH WHITENING KIT</b></div>
        <div class="form__field">Name</div><div class="form__field">Email</div><div class="form__field">Phone</div>
        <div class="form__submit">SUBMIT</div>
      </div>
      <div class="tile tile--band tile--dark">ENJOY UP TO 4 NIGHTS</div>
      <div class="tile" style="height:260px;background:linear-gradient(180deg,#c7a06a,#6a5040)" role="img" aria-label="Resort and casino photo"></div>
    </div>
  </div>
  <svg class="offer-wedge" width="1149" height="530" viewBox="0 0 1149 530" aria-hidden="true">
    <defs>
      <linearGradient id="wedgeFill" x1="0" y1="0" x2="0" y2="1">
        <stop offset="0" stop-color="#d27a06"/>
        <stop offset="1" stop-color="#f0920f"/>
      </linearGradient>
    </defs>
    <path d="M590,0 H1149 V434 C1080,500 960,530 800,528 C700,525 640,470 620,380 C600,290 600,120 590,0Z" fill="url(#wedgeFill)"/>
  </svg>
  <div class="collage-copy">
    <h1 class="headline">BOOST SALES &amp; LEADS<br>OVERNIGHT</h1>
    <p class="subhead">By enticing your customers with<br>free vacation certificates &amp; other<br>high perceived value incentives</p>
    <p class="limited">Get Free Samples Now For A Limited Time !</p>
  </div>
  <a class="cta cta--teal"><span class="cta__label">GET FREE SAMPLES</span><span class="cta__note">100% FREE</span></a>
  <div class="brand-name">Vantelo</div>
</section>

<section class="banner banner--showcase">
  <div class="showcase-backdrop" role="img" aria-label="Faint dark photo backdrop of a busy restaurant"></div>
  <div class="showcase-copy">
    <h2 class="headline">BOOST SALES &amp; LEADS<br>OVERNIGHT</h2>
    <p class="subhead">By enticing your customers with<br>free vacation certificates &amp; other<br>high perceived value incentives</p>
    <p class="limited">Get Free Samples Now For A Limited Time !</p>
  </div>
  <a class="cta cta--orange"><span class="cta__label">GET FREE SAMPLES</span><span class="cta__note">100% FREE</span></a>

  <div class="flyer flyer--signup">
    <div class="signup__photo" role="img" aria-label="Photo of friends dining together"></div>
    <div class="signup__title">GET A<br>FREE SAMPLE</div>
    <div class="signup__lead">ENTER YOUR DETAILS BELOW TO GET<br>YOUR FREE SAMPLE<br><b>$100 RESTAURANT CASH</b></div>
    <div class="signup__field" style="top:110px">Name</div>
    <div class="signup__field" style="top:134px">Email</div>
    <div class="signup__field" style="top:158px">Phone</div>
    <div class="signup__submit">SUBMIT</div>
    <div class="signup__fine">Receive a sample by email, text message and an instant pdf download.</div>
  </div>

  <div class="flyer flyer--restaurant">
    <div class="restaurant__bar">REDEEM OFFER NOW</div>
    <div class="restaurant__photo" role="img" aria-label="Photo of a waitress serving a table of diners"></div>
    <div class="restaurant__foot">$500 RESTAURANT<br>CERTIFICATE</div>
  </div>

  <div class="flyer flyer--earbuds">
    <div class="earbuds__hero" role="img" aria-label="Photo of wireless earbuds and a woman holding a tablet"></div>
    <div class="earbuds__title">ENJOY</div>
    <div class="earbuds__tag">EARBUDS</div>
    <div class="earbuds__band">EXCLUSIVELY FOR : CUSTOMER NAME</div>
    <p class="earbuds__text">You have been rewarded with premium wireless earbuds and charging case.</p>
    <span class="earbuds__label" style="top:246px">FEATURES</span>
    <span class="earbuds__label earbuds__label--red" style="top:300px">HOW CAN WE DO THIS?</span>
    <div class="earbuds__dots" aria-hidden="true"><span></span><span></span><span></span></div>
    <div class="earbuds__cert">Certificate ID<br><strong>#10983-95930</strong><br>Expires 02/29/2020
      <span class="earbuds__url">WWW.PERKHARBOR.COM</span></div>
  </div>
</section>

</body>
</html>
```